Cabling Business Graphic Design for Website

Hi,

We need a three pages designed for a cabling website: http://www.wiremarta.com.au/

1.) Homepage
2.) Category Page
3.) Product Page

Wiremarta is an online wholesaler of Server Racks and Cables.

Wiremarta began in 2006 as an offshoot of a cabling installation company called Voltrinex which has been around since 1993. Through Voltrinex and the industry insight that gave use we saw the need for a direct, online wholesaler.

The problem we found the with the industry is the middle man. It seemed that industry suppliers were so obsessed with carving out distribution channels and establishing exclusive resellers and wholesalers that they began to alienate their products and price themselves out of the market.

Then came Wiremarta - the first direct online data comms wholesaler to hit the industry.

We manufacture, import and sell direct - we have no middle men, keep our prices fair and our product range fresh.

Top three competitors:
Pivotal Brookware - www.dorvane.com.au
Shelvora - www.shelvora.com.au
Quendel Networks - www.quendel.net.au

Our range - we offer a massive range of products - we are always adding new and unique products.

Our Service - we have technical sales staff who are able to help with technical questions and provide advice on how to do things / what to buy - its not just a call centre situation.

We are able to custom manufacture cables and cabinets to suit specifications.

Its very easy to order from us, our turnaround time is 99% of the time 24 hours.

Please refer to the design brief file and the business uncovery for more information. The design brief files are quite specific so please ensure the design adheres to this brief.

Target Market(s)

IT Managers, Electricians, Network Integrators and IT companies.

They have a contract with schools and government departments to order their supplies. This is a massive section of their market.

Industry/Entity Type

Industry

Requirements
Must have
• Reinforce
* that the products adhere to government and industry certifications
* warranty / quality guarantee
* delivery details / stock availability
Nice to have
• Included in the Business Uncovery file
Should not have
• Included in the Business Uncovery

```html
<!DOCTYPE html>
<html lang="en">
<head>
<meta charset="utf-8">
<title>Wiremarta – Product Category</title>
<link href="https://fonts.googleapis.com/css2?family=Arimo:wght@400;700&family=Ubuntu:wght@400;500;700&display=swap" rel="stylesheet">
<style>
:root{
  --lime:#b9d900;
  --lime-dark:#86ad00;
  --green-btn:#8fbf08;
  --ink:#222;
  --dark:#2a2a2a;
  --darker:#1d1d1d;
  --mid:#3a3a3a;
  --red:#cc1f1a;
  --paper:#fff;
  --line:#d9d9d9;
  --grey:#555;
  --panel:#f4f4f4;
}
*{box-sizing:border-box;margin:0;padding:0}
html,body{width:829px;height:1200px;overflow:hidden;background:#fff}
body{font-family:"Arimo",Arial,sans-serif;color:var(--ink);font-size:9px}
.page{position:relative;width:829px;height:1200px;overflow:hidden;
  background:linear-gradient(#2e2e2e 0,#2e2e2e 410px,#8a8a8a 410px,#8a8a8a 950px,var(--dark) 950px)}
.abs{position:absolute}

/* header */
.header{left:0;top:0;width:829px;height:150px;background:linear-gradient(#f2f2f2,#e0e0e0)}
.header-band{left:0;top:0;width:829px;height:112px;background:linear-gradient(180deg,#c9e300,#9cc300)}
.brand-slab{left:-20px;top:-10px;width:250px;height:125px;background:linear-gradient(#2a2a2a,#111);transform:skewY(-4deg);box-shadow:2px 3px 6px rgba(0,0,0,.4)}
.brand{left:12px;top:40px;display:flex;align-items:center;gap:8px;font-weight:700;font-size:34px;color:#fff;letter-spacing:-.5px}
.brand i{display:block;width:18px;height:18px;background:var(--lime)}
.search{left:267px;top:31px;width:321px;height:66px;background:#f6f6f6;border:1px solid #dcdcdc}
.search label{position:absolute;left:9px;top:11px;font-size:11px;letter-spacing:.5px;color:#333}
.search .field{position:absolute;left:9px;top:27px;width:210px;height:24px;background:#fff;border:1px solid #ccc;font-size:10px;color:#999;padding:6px 4px;letter-spacing:.5px}
.search .go{position:absolute;left:237px;top:25px;width:73px;height:28px;border:2px solid #bbb;background:#fff;color:#7fa400;font-size:11px;font-weight:700;text-align:center;line-height:24px}
.chat{left:625px;top:18px;width:157px;height:34px;display:flex;align-items:center}
.chat .avatar{width:34px;height:34px;border-radius:50%;background:linear-gradient(#d86a2a,#a33b12)}
.chat .label{margin-left:-2px;height:30px;width:126px;background:#8ab000;border-radius:3px;color:#fff;font-family:"Ubuntu",sans-serif;font-size:14px;line-height:14px;padding:3px 10px}
.chat .label small{display:block;text-align:right;font-size:11px}
.phone{left:625px;top:73px;width:163px;height:32px;background:#8ab000;border-radius:4px;display:flex;align-items:center;gap:6px;padding-left:6px;color:#fff;font-family:"Ubuntu",sans-serif;font-size:16px}
.login-input{top:119px;height:23px;border:1px solid #ccc;background:#fff;font-size:10px;color:#666;padding:5px 7px}
.login-btn{left:722px;top:117px;width:55px;height:25px;background:#1e1e1e;color:#fff;font-weight:700;font-size:11px;text-align:center;line-height:25px}

/* nav */
.nav{left:5px;top:150px;width:818px;height:42px;background:linear-gradient(#3b3b3b,#1f1f1f);display:flex;align-items:center;border-radius:2px}
.nav a{color:#eee;text-decoration:none;font-size:10px;text-transform:uppercase;letter-spacing:.2px;height:26px;line-height:26px;text-align:center;border-right:1px solid #555}
.nav a:last-child{border-right:0}
.nav a.active{background:var(--green-btn);color:#fff;margin:0 12px 0 64px;width:64px;border-right:0}

/* main panel */
.main{left:13px;top:225px;width:804px;height:773px;background:var(--paper)}

/* sidebar */
.categories{left:22px;top:211px;width:161px;height:422px;background:#fff;border:1px solid #ddd}
.box-head{height:28px;background:linear-gradient(#d9ee23,#9cc300);color:#fff;font-family:"Ubuntu",sans-serif;font-weight:500;font-size:15px;line-height:32px;padding-left:12px;letter-spacing:.3px}
.cat-list{list-style:none;padding:0 8px}
.cat-list li{height:23.3px;line-height:23px;border-bottom:1px solid #e4e4e4;font-size:9px;font-weight:700;color:#333;padding-left:10px;position:relative}
.cat-list li::before{content:"";position:absolute;left:0;top:10px;width:4px;height:4px;background:var(--red)}
.testimonials{left:22px;top:658px;width:161px;height:174px;background:#f7f7f7;border:1px solid #ddd}
.testimonials .box-head{padding-left:58px}
.bubble{position:absolute;left:6px;top:4px}
.testimonials p{padding:30px 8px 0;font-size:9px;line-height:15px;color:#333}
.testimonials b{font-weight:700}
.more-link{position:absolute;right:8px;bottom:9px;font-size:9px;color:#333;text-decoration:underline}

/* content */
.title{left:201px;top:255px;color:var(--red);font-family:"Ubuntu",sans-serif;font-weight:500;font-size:13px;display:flex;align-items:center;gap:6px}
.intro{left:198px;top:286px;width:454px;font-size:9px;line-height:15px;color:#333}
.toolbar{left:197px;top:348px;width:455px;height:32px;border:1px solid #e3e3e3;border-radius:16px;background:#fff}
.sort{position:absolute;left:15px;top:10px;font-size:9px;color:#444}
.sort-select{position:absolute;left:62px;top:4px;width:109px;height:20px;border:1px solid #ccc;background:linear-gradient(#fff,#eee);font-size:10px;padding:4px 18px;color:#222}
.sort-select svg{position:absolute;right:3px;top:5px}
.pager{position:absolute;display:flex;align-items:center;gap:4px}
.pager span{width:14px;height:14px;border-radius:50%;border:1px solid #aaa;font-size:9px;text-align:center;line-height:12px;color:#333;background:#fff}
.pager span.on{background:var(--red);border-color:var(--red);color:#fff}

.product{width:140px;text-align:center}
.thumb{margin:0 auto;width:125px;height:92px;background:#2e2e2e;padding:8px}
.thumb div{width:100%;height:100%}
.t-cable{background:linear-gradient(135deg,#e9e9e9 20%,#c6c6c6 45%,#3d6fc5 50%,#d33 60%,#e9e9e9 80%)}
.t-coil{background:radial-gradient(ellipse at 55% 55%,#2c2c2c 0 30%,#b8c100 34%,#ececec 44%,#dcdcdc)}
.t-box{background:linear-gradient(160deg,#ececec 25%,#1d1d1d 40%,#111 65%,#e6e6e6 80%)}
.t-net{background:linear-gradient(180deg,#e8e8e8 20%,#c62020 45%,#2a56c0 60%,#e6e6e6 85%)}
.t-hdmi{background:radial-gradient(circle at 50% 55%,#2f7fd0 0 22%,#a6b0bb 30%,#ededed 60%)}
.t-lead{background:radial-gradient(ellipse at 40% 50%,#d9d9d9 0 18%,#3a3a3a 22%,#7b7b7b 30%,#ebebeb 48%)}
.stars{margin-top:4px;font-size:10px;letter-spacing:1px;color:#222;line-height:11px}
.pname{font-size:9.5px;font-weight:700;color:#333;text-decoration:underline;letter-spacing:.8px;height:12px}
.price{font-size:8.5px;color:#222;margin-top:2px}
.price b{font-weight:700}
.actions{display:flex;justify-content:center;gap:3px;margin-top:3px}
.btn{height:18px;line-height:18px;border-radius:3px;font-size:8.5px;color:#fff;padding:0 5px;white-space:nowrap}
.btn.dark{background:linear-gradient(#3a3a3a,#111)}
.btn.green{background:linear-gradient(#a9d313,#76a100)}

/* right column */
.cart{left:667px;top:212px;width:140px;height:155px;background:#fff;border:1px solid #e0e0e0}
.cart-head{position:absolute;left:-10px;top:-3px;display:flex;align-items:center;gap:4px;color:#fff;font-size:8px;font-weight:700;white-space:nowrap}
.cart-icon{width:30px;height:30px;border-radius:50%;background:#e9541e;border:2px solid #fff;display:flex;align-items:center;justify-content:center}
.cart-head span{margin-top:12px}
.cart-row{position:absolute;left:19px;width:112px;display:flex;font-size:9px;color:#333}
.cart-row span:nth-child(1){width:76px}
.cart-row span:nth-child(2){width:18px}
.cart-btns{position:absolute;left:9px;top:116px;display:flex;gap:3px}
.cart-btns .btn{height:20px;line-height:20px;font-size:9px;padding:0 6px}
.why{left:668px;top:387px;width:139px;height:67px;background:linear-gradient(90deg,#f1f1f1,#d6d6d6);border:1px solid #ddd}
.why-text{left:740px;top:420px;font-family:"Ubuntu",sans-serif;font-weight:700;line-height:17px;font-size:15px;color:#333}
.why-text em{font-style:normal;color:#d0601a;font-size:13px;font-weight:500}
.certs{left:667px;top:475px;width:141px;height:156px;background:#fff;border:1px solid #ddd}
.certs h3{font-family:"Ubuntu",sans-serif;font-weight:500;font-size:13.5px;line-height:15px;padding:6px 0 0 15px;color:var(--red)}
.certs h3 span{color:#1f3f8c}
.certs small{display:block;font-size:6.5px;text-align:center;margin-top:5px;color:#333}
.badge{position:absolute;top:59px;width:58px;height:74px}
.mailing{left:667px;top:654px;width:141px;height:200px;background:#fff;border:1px solid #ddd}
.mailing .box-head{font-size:11px;padding-left:10px;height:30px;line-height:30px}
.mailing p{padding:8px 0 0 4px;font-size:10px;line-height:15px;color:#333;width:120px}
.mailing p b{font-weight:700}
.mail-icon{position:absolute;right:8px;top:56px}
.mail-input{position:absolute;left:7px;top:114px;width:127px;height:20px;border:1px solid #ccc;font-size:9px;color:#999;padding:4px 11px;letter-spacing:.5px}
.mail-btn{position:absolute;left:20px;top:149px;width:100px;height:22px;background:linear-gradient(#333,#111);color:#fff;font-size:10px;text-align:center;line-height:22px;border-radius:2px}
.privacy{position:absolute;left:20px;top:182px;font-size:9px;color:#222;text-decoration:underline;letter-spacing:.3px}
.security{left:667px;top:869px;font-family:"Ubuntu",sans-serif;font-size:13px;line-height:15px;color:#222;font-weight:500}
.security span{color:#8ab000}
.cards{left:664px;top:905px;width:148px;height:32px;background:#fff;border:1px solid #ccc;display:flex;align-items:center;justify-content:space-around;padding:0 4px}
.cards i{display:block;width:27px;height:16px;border:1px solid #999;border-radius:2px}

/* footer */
.footer-links{left:0;top:1015px;width:829px;text-align:center;font-size:9px;color:#ddd}
.footer-links span{margin:0 4px}
.fcol{font-size:9px;line-height:15px;color:#e8e8e8}
.fcol h4{font-family:"Ubuntu",sans-serif;font-size:9.5px;font-weight:700;color:var(--lime);letter-spacing:.3px;margin-bottom:1px}
.fcol h5{font-family:"Ubuntu",sans-serif;font-size:13px;font-weight:500;color:#fff;margin-bottom:3px}
.fcol ul{list-style:none}
.fcol li::before{content:"▪ ";font-size:7px}
.fcol .u{text-decoration:underline}
.fthumb{left:239px;top:1056px;width:95px;height:86px;border:3px solid var(--lime);background:linear-gradient(135deg,#f2f2f2,#bdbdbd 55%,#efefef)}
.fdivider{left:13px;top:1158px;width:804px;height:1px;background:#444}
.copy{left:23px;top:1166px;font-size:9px;line-height:12px;color:#eee}
.address{left:589px;top:1162px;font-size:9px;line-height:12px;color:#eee}
</style>
</head>
<body>
<div class="page">

  <header class="abs header"></header>
  <div class="abs header-band"></div>
  <div class="abs brand-slab"></div>
  <div class="abs brand"><i></i>Wiremarta</div>

  <form class="abs search">
    <label>SEARCH</label>
    <div class="field">Search Team.......</div>
    <div class="go">SEARCH</div>
  </form>

  <div class="abs chat">
    <div class="avatar" role="img" aria-label="Support agent with headset"></div>
    <div class="label">LIVE CHAT<small>with us !</small></div>
  </div>
  <div class="abs phone">
    <svg width="18" height="22" viewBox="0 0 18 22"><path d="M4 1l3 5-2 2c1 3 3 6 6 8l2-2 4 3-2 4C8 20 1 12 2 3z" fill="#1b1b1b"/></svg>
    +1(500)555 0182
  </div>

  <div class="abs login-input" style="left:535px;width:79px">Username</div>
  <div class="abs login-input" style="left:636px;width:78px;font-weight:700;letter-spacing:1px">.........</div>
  <div class="abs login-btn">Login</div>

  <nav class="abs nav">
    <a class="active">Home</a>
    <a style="width:130px">About Wiremarta</a>
    <a style="width:110px">Shipping</a>
    <a style="width:140px">Wholesale Outlets</a>
    <a style="width:125px">Chat With Us</a>
    <a style="width:110px">My Account</a>
  </nav>

  <main class="abs main"></main>

  <aside class="abs categories">
    <div class="box-head">Categories</div>
    <ul class="cat-list">
      <li>CABLE</li><li>DATA PRODUCTS</li><li>FIBRE PRODUCTS</li><li>COAX PRODUCTS</li>
      <li>SERVER RACK CABINETS</li><li>ELECTRICAL PRODUCTS</li><li>TELEPHONE / VOICE</li>
      <li>PRODUCTS</li><li>TOOLS &amp; TESTERS</li><li>COMPUTER CABLES</li>
      <li>SWITCHES &amp; HARDWARE</li><li>AV WALL PLATES &amp; INSERTS</li>
      <li>PLASMA &amp; LCD BRACKETS</li><li>CABLE DUCTING CONDUIT</li><li>SPECIALS</li>
    </ul>
  </aside>

  <aside class="abs testimonials">
    <div class="box-head">Testimonials</div>
    <svg class="bubble" width="48" height="42" viewBox="0 0 48 42"><rect x="2" y="2" width="26" height="18" rx="7" fill="#555"/><path d="M8 19l-3 8 9-7z" fill="#555"/><rect x="16" y="13" width="28" height="18" rx="7" fill="#777"/><path d="M36 30l4 8-10-7z" fill="#777"/><path d="M22 19h16M22 23h14M22 27h10" stroke="#ddd" stroke-width="1.5"/></svg>
    <p><b>Vestibulum pretium, lectus nec venenatis volutpat, purus lectus</b> ultrices risus, a condi-mentum risus mi et quam. Pel-lentesque auctor fringilla neque. Duis eu massa...</p>
    <span class="more-link">more testimonials ▸</span>
  </aside>

  <h1 class="abs title">Product Category
    <svg width="20" height="14" viewBox="0 0 20 14"><path d="M2 1l6 6-6 6M10 1l6 6-6 6" fill="none" stroke="#111" stroke-width="2.5"/></svg>
  </h1>
  <p class="abs intro"><b>Lorem ipsum dolor sit amet, consectetuer adipiscing elit. Nam nibh.</b> Nunc varius facilisis eros. Sed erat. In in velit quis arcu ornare laoreet. Curabitur adipiscing luctus massa. Integer ut purus ac augue commodo commodo. Nam nec mi eu justo tempor consectetuer. Etiam vitae nisl. In dignissim lacus ut ante.</p>

  <div class="abs toolbar">
    <span class="sort">Sort By :</span>
    <div class="sort-select">Popularity
      <svg width="12" height="10" viewBox="0 0 12 10"><path d="M1 2l5 5 5-5" fill="none" stroke="#333" stroke-width="2"/></svg>
    </div>
    <div class="pager" style="left:297px;top:8px">
      <svg width="10" height="12" viewBox="0 0 10 12"><path d="M8 1L3 6l5 5" fill="none" stroke="#111" stroke-width="2.5"/></svg>
      <span class="on">1</span><span>2</span><span>3</span><span>4</span><span>5</span>
      <svg width="10" height="12" viewBox="0 0 10 12"><path d="M2 1l5 5-5 5" fill="none" stroke="#111" stroke-width="2.5"/></svg>
    </div>
  </div>

  <!-- product grid -->
  <div class="abs product" style="left:198px;top:403px"><div class="thumb"><div class="t-cable" role="img" aria-label="Coloured patch cables"></div></div><div class="stars">★★★★★</div><div class="pname">Product Name</div><div class="price"><b>Our Price</b> : $ 46</div><div class="actions"><span class="btn dark">more details ▸</span><span class="btn green">Add to Cart ▸</span></div></div>
  <div class="abs product" style="left:356px;top:403px"><div class="thumb"><div class="t-coil" role="img" aria-label="Coiled cable"></div></div><div class="stars">★★★★★</div><div class="pname">Cable Management</div><div class="price"><b>Our Price</b> : $ 0.00</div><div class="actions"><span class="btn dark">more details ▸</span><span class="btn green">Add to Cart ▸</span></div></div>
  <div class="abs product" style="left:513px;top:403px"><div class="thumb"><div class="t-box" role="img" aria-label="Black data device"></div></div><div class="stars">★★★★★</div><div class="pname">Data Products</div><div class="price"><b>Our Price</b> : $ 0.00</div><div class="actions"><span class="btn dark">more details ▸</span><span class="btn green">Add to Cart ▸</span></div></div>

  <div class="abs product" style="left:198px;top:580px"><div class="thumb"><div class="t-net" role="img" aria-label="Network cable connectors"></div></div><div class="stars">★★★★★</div><div class="pname">Network Cable</div><div class="price"><b>Our Price</b> : $ 46</div><div class="actions"><span class="btn dark">more details ▸</span><span class="btn green">Add to Cart ▸</span></div></div>
  <div class="abs product" style="left:356px;top:580px"><div class="thumb"><div class="t-hdmi" role="img" aria-label="HDMI and VGA connectors"></div></div><div class="stars">★★★★★</div><div class="pname">HDMI Cable</div><div class="price"><b>Our Price</b> : $ 57</div><div class="actions"><span class="btn dark">more details ▸</span><span class="btn green">Add to Cart ▸</span></div></div>
  <div class="abs product" style="left:513px;top:580px"><div class="thumb"><div class="t-lead" role="img" aria-label="Coiled lead cable"></div></div><div class="stars">★★★★★</div><div class="pname">Cable</div><div class="price"><b>Our Price</b> : $ 40</div><div class="actions"><span class="btn dark">more details ▸</span><span class="btn green">Add to Cart ▸</span></div></div>

  <div class="abs product" style="left:198px;top:750px"><div class="thumb"><div class="t-cable" role="img" aria-label="Coloured patch cables"></div></div><div class="stars">★★★★★</div><div class="pname">Product Name</div><div class="price"><b>Our Price</b> : $ 46</div><div class="actions"><span class="btn dark">more details ▸</span><span class="btn green">Add to Cart ▸</span></div></div>
  <div class="abs product" style="left:356px;top:750px"><div class="thumb"><div class="t-coil" role="img" aria-label="Coiled cable"></div></div><div class="stars">★★★★★</div><div class="pname">Cable Management</div><div class="price"><b>Our Price</b> : $ 0.00</div><div class="actions"><span class="btn dark">more details ▸</span><span class="btn green">Add to Cart ▸</span></div></div>
  <div class="abs product" style="left:513px;top:750px"><div class="thumb"><div class="t-box" role="img" aria-label="Black data device"></div></div><div class="stars">★★★★★</div><div class="pname"></div><div class="price"><b>Our Price</b> : $ 0.00</div><div class="actions"><span class="btn dark">more details ▸</span><span class="btn green">Add to Cart ▸</span></div></div>

  <div class="abs toolbar" style="top:922px">
    <div class="pager" style="left:297px;top:8px">
      <svg width="10" height="12" viewBox="0 0 10 12"><path d="M8 1L3 6l5 5" fill="none" stroke="#111" stroke-width="2.5"/></svg>
      <span class="on">1</span><span>2</span><span>3</span><span>4</span><span>5</span>
      <svg width="10" height="12" viewBox="0 0 10 12"><path d="M2 1l5 5-5 5" fill="none" stroke="#111" stroke-width="2.5"/></svg>
    </div>
  </div>

  <!-- right column -->
  <div class="abs cart">
    <div class="cart-head">
      <div class="cart-icon"><svg width="18" height="15" viewBox="0 0 18 15"><path d="M1 1h3l2 9h9l2-6H5" fill="none" stroke="#fff" stroke-width="1.8"/><circle cx="7" cy="13" r="1.5" fill="#fff"/><circle cx="14" cy="13" r="1.5" fill="#fff"/></svg></div>
      <span>ONLINE SHOPPING CART</span>
    </div>
    <div class="cart-row" style="top:52px"><span>Amount</span><span>:</span><span>$67</span></div>
    <div class="cart-row" style="top:71px"><span>Sub Total</span><span>:</span><span>$67</span></div>
    <div class="cart-btns"><span class="btn dark">▸ View cart</span><span class="btn green">▸ Check out</span></div>
  </div>

  <div class="abs why" role="img" aria-label="Question mark figure and support person"></div>
  <div class="abs why-text"><em>WHY</em><br>CLIENT</div>

  <section class="abs certs">
    <h3>Certifications &amp;<br><span>Quality Assurance</span></h3>
    <small>QUALITY ASSURED COMPANY</small>
    <div class="badge" style="left:8px;background:#c8171c"></div>
    <div class="badge" style="left:74px;border:1px dashed #1f3f8c;background:#eef1f8"></div>
  </section>

  <section class="abs mailing">
    <div class="box-head">JOIN OUR MAILING LOST</div>
    <p><b>Discover</b> exclusive offers, Products Previews and much more...</p>
    <svg class="mail-icon" width="30" height="30" viewBox="0 0 30 30"><rect x="3" y="9" width="24" height="17" rx="2" fill="#bcd5f0" stroke="#4a7fc0"/><path d="M3 10l12 9 12-9" fill="none" stroke="#4a7fc0"/><circle cx="17" cy="8" r="6" fill="none" stroke="#4a7fc0" stroke-width="1.5"/></svg>
    <div class="mail-input">Your Email Address</div>
    <div class="mail-btn">Get Special Offers</div>
    <span class="privacy">We value your privacy</span>
  </section>

  <div class="abs security"><span>Security &amp;</span><br>Credit Card Notice</div>
  <div class="abs cards">
    <i style="background:#e35a1c"></i><i style="background:#1b3e94"></i><i style="background:#3b6fb8"></i><i style="background:#dfe6f2"></i>
  </div>

  <!-- footer -->
  <div class="abs footer-links">
    <span>Home</span>|<span>About Wiremarta</span>|<span>My Account</span>|<span>Order Status</span>|<span>Wish List</span>|<span>Gift Certificate</span>|<span>View Cart</span>|<span>Sign In</span>|<span>An Account</span>
  </div>

  <div class="abs fcol" style="left:67px;top:1063px">
    <h4>FIBRE PRODUCTS</h4>
    Multimode Fibre Optic Patch Cables<br>Single Mode Fibre Optic Patch Leads<br>Fibre Optic Cable
  </div>
  <div class="abs fthumb" role="img" aria-label="Grey lead cable"></div>
  <div class="abs fcol" style="left:348px;top:1074px">
    <ul><li class="u">Cat5e Patch Panel</li><li class="u">Cat 6 Patch Panels</li></ul>
  </div>
  <div class="abs fcol" style="left:506px;top:1056px">
    <h5>About Wiremarta</h5>
    <ul><li>Multimode Fibre Optic Patch</li><li>Cables Single Mode Fibre</li><li>Optic Patch Leads</li><li>Fibre Optic Cable</li></ul>
  </div>
  <div class="abs fcol" style="left:699px;top:1061px">
    <h4>PATCH PANELS</h4>
    Cat5e Patch Panel<br>Cat 6 Patch Panels
  </div>

  <div class="abs fdivider"></div>
  <div class="abs copy">Copyright 2010 Wiremarta</div>
  <div class="abs address">No. 9, 54 Harlow Lane, Redbank, NSW, 2031<br>Telephone: 61 2 9000 1275, Fax: 61 2 9000 1276,<br>E-Mail: sales@wiremarta.com.au ABN #00 000 000 000</div>

</div>
</body>
</html>
```